Business Card Design Project

Business card design for an IT Service company. A logo has already been created in a different contest and has been attached to this project. Ideally we're looking for a double sided business card that matches the look and feel of our newly created logo.

We're open to creativity if you feel a tag line is needed such as "IT Services and Application Development". We're open to really and look and feel - even single sided business cards if you feel you have something that's a great idea.

Last thought here - I'm not sure how it'll look but maybe a two tone card? One side dark blue and the other side white? Don't limit the design submissions to this tho - just curious if it would look good

Nothing too busy please - simple... Thank you and happy designing!

Target Market(s)

Businesses that require IT Services and support for hosted services, technical consultation, web design.

Industry/Entity Type

Business

Font styles to use
Sans Serif

Requirements
Must have
• Use the colors provided in the logo (see attachment) or additional colors that compliment
Must have the following contact info (not necessarily in this order):
- Alan Fisk
- Founding Partner
- afisk@quillbarrow.example
- 555-382-1946
- www.quillbarrow.example

```html
<!DOCTYPE html>
<html lang="en">
<head>
<meta charset="utf-8">
<title>Quillbarrow – Business Card</title>
<link rel="stylesheet" href="https://fonts.googleapis.com/css2?family=Arimo:ital,wght@0,400;0,700;1,400&display=swap">
<style>
  :root {
    --navy: #061244;
    --blue: #2a7de1;
    --paper: #ffffff;
    --band-text: #ffffff;
  }
  * { margin: 0; padding: 0; box-sizing: border-box; }
  html, body {
    width: 1200px;
    height: 734px;
    overflow: hidden;
    background: var(--paper);
  }
  .card {
    position: relative;
    width: 1200px;
    height: 734px;
    background: var(--paper);
    font-family: "Arimo", Arial, Helvetica, sans-serif;
    color: var(--navy);
  }
  .brand {
    position: absolute;
    top: 120px;
    left: 0;
    width: 100%;
    display: flex;
    justify-content: center;
    align-items: center;
    gap: 28px;
  }
  .brand-square {
    width: 74px;
    height: 74px;
    background: var(--blue);
  }
  .brand-name {
    font-size: 104px;
    font-weight: 700;
    line-height: 1;
    letter-spacing: -1px;
    color: var(--navy);
  }
  .person {
    position: absolute;
    top: 354px;
    left: 0;
    width: 100%;
    text-align: center;
  }
  .person-name {
    font-size: 52px;
    font-weight: 400;
    line-height: 1.1;
  }
  .person-title {
    font-size: 35px;
    font-weight: 400;
    line-height: 1.2;
    margin-top: 2px;
  }
  .contact-band {
    position: absolute;
    top: 575px;
    left: 0;
    width: 100%;
    height: 84px;
    background: var(--navy);
    display: flex;
    justify-content: center;
    align-items: center;
    gap: 42px;
    color: var(--band-text);
    font-size: 26px;
  }
  .contact-item .label {
    font-weight: 700;
    margin-right: 10px;
  }
  .contact-item .value {
    font-style: italic;
  }
</style>
</head>
<body>
  <main class="card">
    <header class="brand">
      <span class="brand-square" aria-hidden="true"></span>
      <span class="brand-name">Quillbarrow</span>
    </header>

    <section class="person">
      <h1 class="person-name">Alan Fisk</h1>
      <p class="person-title">Founding Partner</p>
    </section>

    <footer class="contact-band">
      <span class="contact-item"><span class="label">T</span><span class="value">555-382-1946</span></span>
      <span class="contact-item"><span class="label">E</span><span class="value">afisk@quillbarrow.example</span></span>
      <span class="contact-item"><span class="label">W</span><span class="value">www.quillbarrow.example</span></span>
    </footer>
  </main>
</body>
</html>
```